Sales Leaning Business Card for a Restoration Company - Construction Company
Halvorn Renewal, Inc.
Professional
Benedict L Marlowe Jr
President
318 Fenwirk Ave
Lake Dallas, TX 75065
bmarlowe@hnwok-example.com
www.hnwok-example.com
I would like the card to be more of a salesman's card. Should look professional but lean a bit more towards a sales tool.
24 Hour emergency Services
Water & Fire Damage Restoration
Water Removal and Structural Drying
Storm Damage
Hail / Roofing Damage
Post Mitigation Reconstruction
QNV Accredited
PSTAW Certified

```html
<!DOCTYPE html>
<html lang="en">
<head>
<meta charset="utf-8">
<title>Halvorn Renewal, Inc. – Stationery</title>
<link rel="stylesheet" href="https://fonts.googleapis.com/css2?family=Montserrat:wght@500;700&display=swap">
<style>
  :root{
    --backdrop:#eceeef;
    --paper:#ffffff;
    --brand-deep:#174a68;
    --brand-mid:#2a7ba3;
    --arc-grey:#8d9296;
    --ink:#3f4448;
    --ink-soft:#8a8f93;
    --faint:#e9edf0;
  }
  *{box-sizing:border-box;margin:0;padding:0}
  html,body{width:1200px;height:936px;overflow:hidden;background:var(--backdrop)}
  body{position:relative;font-family:"Montserrat",Arial,sans-serif;color:var(--ink)}
  .piece{position:absolute;background:var(--paper);box-shadow:0 2px 6px rgba(0,0,0,.12);overflow:hidden}
  .piece svg.swoosh{position:absolute;inset:0;width:100%;height:100%}
  .brand{position:absolute;display:flex;align-items:center;gap:8px}
  .brand-dot{border-radius:50%;background:var(--brand-deep);flex:none}
  .brand-name{font-weight:700;color:var(--brand-deep);letter-spacing:.04em;line-height:1.05}
  .small{position:absolute;font-size:7px;line-height:1.45;color:var(--ink-soft);font-weight:500}

  .letterhead{left:177px;top:76px;width:410px;height:526px}
  .letterhead .brand{left:22px;top:34px}
  .letterhead .brand-dot{width:22px;height:22px}
  .letterhead .brand-name{font-size:13px}
  .letterhead .mark-faint{position:absolute;left:145px;top:188px;width:120px;height:120px;border-radius:50%;background:var(--faint)}
  .letterhead .contact{left:22px;top:392px}

  .sheet{left:633px;top:35px;width:475px;height:567px}
  .sheet .brand{left:0;right:0;top:250px;flex-direction:column;gap:10px}
  .sheet .brand-dot{width:66px;height:66px}
  .sheet .brand-name{font-size:34px;text-align:center}

  .card-front{left:40px;top:653px;width:203px;height:76px}
  .card-front .brand{left:8px;top:12px;gap:5px}
  .card-front .brand-dot{width:12px;height:12px}
  .card-front .brand-name{font-size:8px}
  .card-front .details{right:8px;top:38px;font-size:4.5px;line-height:1.4;text-align:right}
  .card-front .person{color:var(--brand-deep);font-weight:700}
  .card-front .emergency{left:8px;top:40px;font-size:5px;line-height:1.3;font-weight:700;color:var(--brand-deep)}

  .card-back{left:40px;top:759px;width:203px;height:81px}
  .card-back .mark{position:absolute;left:12px;top:20px;width:34px;height:34px;border-radius:50%;background:var(--brand-deep)}
  .card-back .services{position:absolute;left:58px;top:6px;width:138px;font-size:4.5px;line-height:1.4;color:var(--ink);font-weight:500}
  .card-back .services h2{font-size:5px;font-weight:700;color:var(--brand-deep);letter-spacing:.04em;margin-bottom:1px}
  .card-back .services ul{list-style:none}
  .card-back .services li::before{content:"";display:inline-block;width:2px;height:2px;border-radius:50%;background:var(--brand-mid);margin-right:3px;vertical-align:middle}
  .card-back .credentials{display:flex;gap:8px;margin-top:2px;font-weight:700;color:var(--brand-deep)}
  .card-back .credentials span{display:flex;align-items:center;gap:2px}
  .card-back .badge{width:5px;height:5px;background:var(--brand-mid);flex:none}

  .envelope{left:263px;top:663px;width:334px;height:172px}
  .envelope .brand{left:14px;top:20px;gap:6px}
  .envelope .brand-dot{width:18px;height:18px}
  .envelope .brand-name{font-size:12px}
  .envelope .return{left:14px;top:52px;font-size:5px}

  .envelope-back{left:633px;top:663px;width:475px;height:172px}
  .envelope-back .web{position:absolute;left:0;right:0;top:20px;text-align:center;font-size:7px;letter-spacing:.3em;color:#fff;font-weight:500}
</style>
</head>
<body>

<section class="piece letterhead" aria-label="Letterhead">
  <svg class="swoosh" viewBox="0 0 100 100" preserveAspectRatio="none" aria-hidden="true">
    <defs><linearGradient id="lhBand" x1="0" x2="1"><stop offset="0" stop-color="var(--brand-mid)"/><stop offset="1" stop-color="var(--brand-deep)"/></linearGradient></defs>
    <path d="M35,0 H100 V26 C82,12 60,3 35,0 Z" fill="url(#lhBand)"/>
    <path d="M28,0 C58,3 84,14 100,30" fill="none" stroke="var(--arc-grey)" stroke-width=".5"/>
  </svg>
  <div class="brand"><span class="brand-dot"></span><span class="brand-name">HALVORN<br>RENEWAL</span></div>
  <div class="mark-faint"></div>
  <div class="small contact">318 Fenwirk Ave<br>Lake Dallas, TX 75065<br>P (940) 555-0142<br>F (940) 555-0187<br>bmarlowe@hnwok-example.com<br>www.hnwok-example.com</div>
</section>

<section class="piece sheet" aria-label="Presentation sheet">
  <svg class="swoosh" viewBox="0 0 100 100" preserveAspectRatio="none" aria-hidden="true">
    <defs><linearGradient id="shBand" x1="0" x2="1"><stop offset="0" stop-color="var(--brand-mid)"/><stop offset="1" stop-color="var(--brand-deep)"/></linearGradient></defs>
    <path d="M0,0 H100 V11 C70,4 35,3 0,6 Z" fill="url(#shBand)"/>
    <path d="M0,9 C35,5 70,7 100,14" fill="none" stroke="var(--arc-grey)" stroke-width=".5"/>
  </svg>
  <div class="brand"><span class="brand-dot"></span><span class="brand-name">HALVORN<br>RENEWAL</span></div>
</section>

<section class="piece card-front" aria-label="Business card front">
  <svg class="swoosh" viewBox="0 0 100 100" preserveAspectRatio="none" aria-hidden="true">
    <defs><linearGradient id="cfBand" x1="0" x2="1"><stop offset="0" stop-color="var(--brand-mid)"/><stop offset="1" stop-color="var(--brand-deep)"/></linearGradient></defs>
    <path d="M45,0 H100 V45 C85,22 68,6 45,0 Z" fill="url(#cfBand)"/>
    <path d="M38,0 C65,6 86,24 100,52" fill="none" stroke="var(--arc-grey)" stroke-width=".8"/>
  </svg>
  <div class="brand"><span class="brand-dot"></span><span class="brand-name">HALVORN<br>RENEWAL</span></div>
  <div class="small emergency">24 HOUR EMERGENCY<br>(940) 555-0142</div>
  <div class="small details"><span class="person">Benedict L Marlowe Jr</span><br>President<br>318 Fenwirk Ave, Lake Dallas, TX 75065<br>bmarlowe@hnwok-example.com<br>www.hnwok-example.com</div>
</section>

<section class="piece card-back" aria-label="Business card back">
  <svg class="swoosh" viewBox="0 0 100 100" preserveAspectRatio="none" aria-hidden="true">
    <path d="M0,100 H100 V88 C65,96 30,97 0,92 Z" fill="var(--brand-deep)"/>
  </svg>
  <div class="mark"></div>
  <div class="services">
    <h2>24 HOUR EMERGENCY SERVICES</h2>
    <ul>
      <li>Water &amp; Fire Damage Restoration</li>
      <li>Water Removal and Structural Drying</li>
      <li>Storm Damage</li>
      <li>Hail / Roofing Damage</li>
      <li>Post Mitigation Reconstruction</li>
    </ul>
    <div class="credentials">
      <span><i class="badge"></i>QNV Accredited</span>
      <span><i class="badge"></i>PSTAW Certified</span>
    </div>
  </div>
</section>

<section class="piece envelope" aria-label="Envelope front">
  <svg class="swoosh" viewBox="0 0 100 100" preserveAspectRatio="none" aria-hidden="true">
    <defs><linearGradient id="enBand" x1="0" x2="1"><stop offset="0" stop-color="var(--brand-mid)"/><stop offset="1" stop-color="var(--brand-deep)"/></linearGradient></defs>
    <path d="M40,0 H100 V38 C82,16 62,4 40,0 Z" fill="url(#enBand)"/>
    <path d="M33,0 C62,5 85,20 100,44" fill="none" stroke="var(--arc-grey)" stroke-width=".5"/>
  </svg>
  <div class="brand"><span class="brand-dot"></span><span class="brand-name">HALVORN<br>RENEWAL</span></div>
  <div class="small return">318 Fenwirk Ave Lake Dallas, TX 75065</div>
</section>

<section class="piece envelope-back" aria-label="Envelope back">
  <svg class="swoosh" viewBox="0 0 100 100" preserveAspectRatio="none" aria-hidden="true">
    <defs><linearGradient id="ebBand" x1="0" x2="1"><stop offset="0" stop-color="var(--brand-deep)"/><stop offset=".5" stop-color="var(--brand-mid)"/><stop offset="1" stop-color="var(--brand-deep)"/></linearGradient></defs>
    <path d="M0,0 H100 V30 C70,44 30,44 0,30 Z" fill="url(#ebBand)"/>
    <path d="M0,34 C30,48 70,48 100,34" fill="none" stroke="var(--arc-grey)" stroke-width=".5"/>
  </svg>
  <div class="web">WWW.HNWOK-EXAMPLE.COM</div>
</section>

</body>
</html>
```